TITLE: What Lifts a Young Player Past the Bench? SUB-TITLE: A Family’s Plain Talk Manual for Coaching...

My book is for parents who have young children that are really into sports. My book empowers parents so they can motivate their children to succeed. It deals with sports psychology. Both my title and subtitle should be easy to read. Ideally, I would like a picture of young athlete(s) on the title. I have uploaded files of some books on Brindlemart that deal with the same subject. The last two files are 1) my company logo, please try to include these colors 2) an ebook cover I put together myself. You will notice an On-line bonus in the middle of the book, this Bonus needs to be on the cover.

Target Market(s)

Parents with children who play sports at a high level

Colors

Designer to choose colors to be used in the design.

Requirements
Must have
• Online Bonus feature as per my example.
• Dimensions: Paperlyn = The ideal size of your eBook cover art is a height/width ratio of 1.6:1. This means that for every 1,000 pixels in width, the image should be 1,600 pixels in height.
Nice to have
• picture of a young athlete or young athletes

```html
<!DOCTYPE html>
<html lang="en">
<head>
<meta charset="utf-8">
<title>What Lifts a Young Player Past the Bench? — eBook Cover</title>
<link rel="stylesheet" href="https://fonts.googleapis.com/css2?family=Montserrat:wght@300;600;800;900&family=Bangers&display=swap">
<style>
  :root {
    --backdrop: #9a9ea1;
    --paper: #ffffff;
    --ink: #3e3631;
    --orange: #f29a1f;
    --orange-deep: #e06a1b;
    --badge-ring: #f5b23c;
    --photo-light: #eceae6;
    --photo-mid: #d7b79a;
  }
  * { box-sizing: border-box; margin: 0; padding: 0; }
  html, body { width: 1200px; height: 1200px; overflow: hidden; }
  body { background: var(--backdrop); position: relative; font-family: "Montserrat", sans-serif; }

  .cover {
    position: absolute; left: 270px; top: 72px;
    width: 660px; height: 1056px;
    background: var(--paper);
    box-shadow: 0 6px 18px rgba(0,0,0,.18);
    overflow: hidden;
  }

  .title-lead {
    position: absolute; top: 68px; left: 0; width: 100%;
    text-align: center; font-weight: 300; font-size: 36px;
    letter-spacing: 14px; line-height: 1; color: var(--ink);
  }
  .title-main {
    position: absolute; top: 114px; left: 0; width: 100%;
    text-align: center; font-weight: 900; font-size: 66px;
    letter-spacing: -3px; line-height: 1; color: var(--ink);
    transform: scaleY(1.3); transform-origin: top center;
  }
  .title-end {
    position: absolute; top: 222px; left: 0; width: 100%;
    text-align: center; font-weight: 800; font-size: 48px;
    letter-spacing: -2px; line-height: 1; color: var(--orange);
  }

  .athlete-photo {
    position: absolute; left: 150px; top: 318px;
    width: 268px; height: 450px;
    border-radius: 46% 40% 8% 8% / 22% 22% 4% 4%;
    background: radial-gradient(ellipse at 50% 30%, var(--photo-mid) 0%, #e6d3c2 45%, var(--photo-light) 80%, var(--paper) 100%);
  }

  .bonus-badge { position: absolute; left: 422px; top: 286px; width: 170px; height: 170px; }
  .bonus-text {
    position: absolute; left: 422px; top: 286px; width: 170px; height: 170px;
    display: flex; flex-direction: column; align-items: center; justify-content: center;
    color: var(--ink); text-align: center; line-height: 1;
  }
  .bonus-free { font-weight: 600; font-size: 20px; }
  .bonus-small { font-weight: 600; font-size: 8px; margin-top: 1px; }
  .bonus-price { font-weight: 800; font-size: 34px; letter-spacing: -1px; margin-top: 2px; }
  .bonus-value { font-weight: 600; font-size: 18px; margin-top: -2px; }
  .bonus-note { font-size: 6px; margin-top: 3px; }

  .brand {
    position: absolute; left: 96px; top: 712px;
    display: flex; align-items: center; gap: 10px;
  }
  .brand-dot { width: 44px; height: 44px; border-radius: 50%; background: var(--orange); }
  .brand-name { font-weight: 600; font-size: 15px; color: var(--ink); }

  .subtitle {
    position: absolute; top: 800px; left: 0; width: 100%;
    text-align: center; font-family: "Bangers", sans-serif; line-height: 1;
  }
  .subtitle span { display: block; paint-order: stroke fill; }
  .sub-lead {
    font-size: 30px; color: var(--ink); letter-spacing: 0.5px;
    -webkit-text-stroke: 5px var(--paper);
    text-shadow: 0 2px 4px rgba(0,0,0,.35);
  }
  .sub-main {
    font-size: 62px; color: var(--orange); letter-spacing: 1px; margin-top: 2px;
    -webkit-text-stroke: 4px var(--ink);
    text-shadow: 0 3px 6px rgba(0,0,0,.4);
  }
  .sub-emph {
    font-size: 52px; color: var(--orange); letter-spacing: 1px;
    -webkit-text-stroke: 4px var(--ink);
    text-shadow: 0 3px 6px rgba(0,0,0,.4);
  }
  .sub-tail {
    font-size: 30px; color: var(--ink); letter-spacing: 0.5px; margin-top: 2px;
    -webkit-text-stroke: 5px var(--paper);
    text-shadow: 0 2px 4px rgba(0,0,0,.35);
  }
</style>
</head>
<body>
  <main class="cover">
    <p class="title-lead">WHAT LIFTS A</p>
    <h1 class="title-main">YOUNG PLAYER</h1>
    <p class="title-end">PAST THE BENCH?</p>

    <div class="athlete-photo" role="img" aria-label="Photo of a teenage runner in a white and green singlet, mid-stride"></div>

    <svg class="bonus-badge" viewBox="0 0 174 174" aria-hidden="true">
      <g fill="var(--orange-deep)">
        <rect x="27" y="27" width="120" height="120" transform="rotate(0 87 87)"/>
        <rect x="27" y="27" width="120" height="120" transform="rotate(15 87 87)"/>
        <rect x="27" y="27" width="120" height="120" transform="rotate(30 87 87)"/>
        <rect x="27" y="27" width="120" height="120" transform="rotate(45 87 87)"/>
        <rect x="27" y="27" width="120" height="120" transform="rotate(60 87 87)"/>
        <rect x="27" y="27" width="120" height="120" transform="rotate(75 87 87)"/>
      </g>
      <circle cx="87" cy="87" r="68" fill="var(--badge-ring)"/>
      <circle cx="87" cy="87" r="58" fill="var(--orange)"/>
    </svg>
    <div class="bonus-text">
      <span class="bonus-free">FREE</span>
      <span class="bonus-small">ONLINE<br>WORKSHOP</span>
      <span class="bonus-price">$170</span>
      <span class="bonus-value">VALUE</span>
      <span class="bonus-note">Details Inside</span>
    </div>

    <div class="brand">
      <span class="brand-dot"></span>
      <span class="brand-name">Steady Mind Coaching</span>
    </div>

    <h2 class="subtitle">
      <span class="sub-lead">A FAMILY’S PLAIN TALK</span>
      <span class="sub-main">MANUAL FOR COACHING</span>
      <span class="sub-emph">CONFIDENT</span>
      <span class="sub-tail">FOCUSED AND RESILIENT ATHLETES</span>
    </h2>
  </main>
</body>
</html>
```